Healthcare Information Interoperability Effort Needs a Roadmap Graphic

Interoperability of healthcare information is critical to accelerated research and improved patient outcomes. We are seeking a graphic to illustrate our roadmap for achieving healthcare information interoperability.

The roadmap has four key components. Please refer to this link for more information about direction and guide in the presentation.
https://lnkvyro.example/q7Zp3m

Industry/Entity Type

Healthcare

Font styles to use
Sans Serif

Requirements
Must have
• See https://lnkvyro.example/q7Zp3m
Nice to have

```html
<!DOCTYPE html>
<html lang="en">
<head>
<meta charset="utf-8">
<title>Roadmap to Semantic Interoperability</title>
<link href="https://fonts.googleapis.com/css2?family=Mulish:ital,wght@1,400;1,700&display=swap" rel="stylesheet">
<style>
  :root {
    --sky-top: #a9d7e6;
    --sky-bottom: #e4f2f7;
    --road: #3f4a4b;
    --lane: #ffffff;
    --orange: #f2ab3c;
    --red: #d9566b;
    --cyan: #5de3ee;
    --yellow: #f5cc55;
    --green: #4a6a4b;
    --cream: #f7efd8;
    --ink: #1f2a2e;
    --ink-soft: #f3f6f6;
    --hub-fill: #e6f3f8;
    --brand: #1f6fd6;
  }
  html, body { margin: 0; padding: 0; overflow: hidden; }
  body { width: 1200px; height: 679px; }
  .roadmap {
    position: relative;
    width: 1200px;
    height: 679px;
    overflow: hidden;
    font-family: "Mulish", sans-serif;
  }
  .roadmap__backdrop {
    position: absolute; inset: 0;
    background: radial-gradient(ellipse at 45% 45%, var(--sky-bottom) 0%, #cfe8f1 45%, var(--sky-top) 100%);
  }
  .roadmap__art { position: absolute; inset: 0; }
  .brand {
    position: absolute; left: 118px; top: 192px;
    display: flex; align-items: center; gap: 8px;
    font-size: 18px; font-style: italic; color: var(--ink);
  }
  .brand__mark { width: 14px; height: 14px; background: var(--brand); }
  .milestone {
    position: absolute;
    margin: 0;
    font-size: 16.5px;
    font-style: italic;
    line-height: 1.35;
    color: var(--ink);
    white-space: nowrap;
  }
  .milestone--on-road { color: var(--ink-soft); }
  .milestone--standard { font-weight: 700; font-size: 15px; line-height: 1.45; }
  .milestone__lead { color: var(--ink); }
  .hub-label {
    position: absolute; left: 982px; top: 362px; width: 200px;
    text-align: center; font-style: italic;
    font-size: 15px; line-height: 1.4; color: var(--ink);
  }
</style>
</head>
<body>
<main class="roadmap">
  <div class="roadmap__backdrop" role="img" aria-label="Soft blue background with faint sketched doodles of light bulbs, clouds, atoms, paper planes and stationery"></div>

  <svg class="roadmap__art" width="1200" height="679" viewBox="0 0 1200 679" aria-hidden="true">
    <defs>
      <path id="pin" d="M0,0 C-7,-14 -22,-26 -22,-41 A22,22 0 1 1 22,-41 C22,-26 7,-14 0,0Z"/>
    </defs>

    <rect class="road" x="0" y="333" width="1200" height="108" fill="var(--road)"/>
    <line class="road__lane" x1="0" y1="389" x2="1200" y2="389" stroke="var(--lane)" stroke-width="3" stroke-dasharray="16 10"/>

    <g class="hub">
      <circle cx="1082" cy="389" r="98" fill="var(--hub-fill)"/>
      <path d="M1002,332 A98,98 0 0 1 1142,312" fill="none" stroke="#fff" stroke-width="4"/>
      <path d="M1142,312 l-14,-2 m14,2 l-6,12" stroke="#fff" stroke-width="4" fill="none" stroke-linecap="round"/>
      <path d="M1162,446 A98,98 0 0 1 1022,466" fill="none" stroke="#fff" stroke-width="4"/>
      <path d="M1022,466 l14,2 m-14,-2 l6,-12" stroke="#fff" stroke-width="4" fill="none" stroke-linecap="round"/>
    </g>

    <g class="leaders" stroke-width="1.5">
      <line x1="52" y1="306" x2="87" y2="255" stroke="var(--orange)"/>
      <line x1="168" y1="395" x2="204" y2="345" stroke="var(--red)"/>
      <line x1="374" y1="303" x2="408" y2="252" stroke="var(--cyan)"/>
      <line x1="490" y1="393" x2="525" y2="342" stroke="var(--yellow)"/>
      <line x1="696" y1="301" x2="729" y2="251" stroke="var(--green)"/>
      <line x1="810" y1="391" x2="846" y2="342" stroke="var(--cyan)"/>
    </g>
    <g class="leader-dots" stroke="#fff" stroke-width="2">
      <circle cx="87" cy="255" r="5" fill="var(--orange)"/>
      <circle cx="204" cy="345" r="5" fill="var(--red)"/>
      <circle cx="408" cy="252" r="5" fill="var(--cyan)"/>
      <circle cx="525" cy="342" r="5" fill="var(--yellow)"/>
      <circle cx="729" cy="251" r="5" fill="var(--green)"/>
      <circle cx="846" cy="342" r="5" fill="var(--cyan)"/>
    </g>

    <g class="pin" transform="translate(42,344)">
      <ellipse rx="18" ry="3" fill="#000" opacity="0.25"/>
      <use href="#pin" fill="var(--orange)"/>
      <circle cy="-41" r="12" fill="var(--cream)"/><circle cy="-41" r="5" fill="var(--orange)"/>
    </g>
    <g class="pin" transform="translate(159,432)">
      <ellipse rx="18" ry="3" fill="#000" opacity="0.25"/>
      <use href="#pin" fill="var(--red)"/>
      <circle cy="-41" r="12" fill="var(--cream)"/><circle cy="-41" r="5" fill="var(--green)"/>
    </g>
    <g class="pin" transform="translate(364,341)">
      <ellipse rx="18" ry="3" fill="#000" opacity="0.25"/>
      <use href="#pin" fill="var(--cyan)"/>
      <circle cy="-41" r="12" fill="var(--cream)"/><circle cy="-41" r="5" fill="var(--cyan)"/>
    </g>
    <g class="pin" transform="translate(481,431)">
      <ellipse rx="18" ry="3" fill="#000" opacity="0.25"/>
      <use href="#pin" fill="var(--yellow)"/>
      <circle cy="-41" r="12" fill="var(--cream)"/><circle cy="-41" r="5" fill="var(--yellow)"/>
    </g>
    <g class="pin" transform="translate(686,339)">
      <ellipse rx="18" ry="3" fill="#000" opacity="0.25"/>
      <use href="#pin" fill="var(--green)"/>
      <circle cy="-41" r="12" fill="var(--cream)"/><circle cy="-41" r="5" fill="var(--green)"/>
    </g>
    <g class="pin" transform="translate(801,429)">
      <ellipse rx="18" ry="3" fill="#000" opacity="0.25"/>
      <use href="#pin" fill="var(--cyan)"/>
      <circle cy="-41" r="12" fill="var(--cream)"/><circle cy="-41" r="5" fill="var(--cyan)"/>
    </g>
  </svg>

  <div class="brand"><span class="brand__mark"></span>Quorvane</div>

  <p class="milestone" style="left:98px; top:244px;">RDF as a Universal<br>Information<br>Representation</p>
  <p class="milestone milestone--on-road" style="left:214px; top:334px;">RDF Mappings</p>
  <p class="milestone" style="left:419px; top:242px;">Translations between<br>models &amp; vocabularies</p>
  <p class="milestone milestone--on-road" style="left:535px; top:334px;">Crowd-Sourced<br>Translation Rules</p>
  <p class="milestone milestone--standard" style="left:740px; top:242px;">RDF/ OWL<br>Standards<br>Definitions</p>
  <p class="milestone milestone--on-road" style="left:859px; top:310px;"><span class="milestone__lead">Collaborative</span><br>Standards<br>Convergence</p>

  <div class="hub-label">SEMANTIC<br>INTEROPERABILITY</div>
</main>
</body>
</html>
```